Norwegian psychologist service needs a fresh and exiting web site*

Norwegian psychologist service: working with therapy, personal development, mastery and personal growth. Focus: children and teenagers with special needs; family dynamics; group processes; individuals with a need for therapy and personal growth. (Our company name: Fjordlys og samhold (means Mastery and Growth).

We already have a logo for the company, which will be used (will be attached in the project).

The webside is to be structured in 4 pages with roll down curtain menus (the numbers are just for guiding the designer - the should not be added):

Page 1: Om Fjordlys og Samhold (about Mastery and Growth): this is where our business is is presented/described shortly: Lorem Ipsum dolor cit...

Page 2: Tjenester (Services): this is where our 5 service areas are presented:
2.1 Utredning (Investigation, diagnosing): Lorem Ipsum dolor cit...
2.2 Rådgivning (consulting): Lorem Ipsum dolor cit...

2.3 Kurs og work shops (courses and work shops): Lorem Ipsum dolor cit...
2.3a Fjordlys og samhold Tema 1 (T1)
2.3b Fjordlys og samhold Tema 2 (T2)
2.3c Fjordlys og samhold Tema 3 (T3)

2.4 Terapi og utvikling (Therapy and development)
2.4a Fjordlys og samhold for individer (FS1)
2.4b Fjordlys og samhold i familier (FS2)
2.4c Fjordlys og samhold i grupper (FS3)
2.4d Fjordlys og samhold i institusjoner (FS4)

Page 3: Aktuelt (Blog): this is our blog where we share knowledge and articles

Page 4: Kontakt (Contact): This is the contact form page. Contact form should constitute:
- Ditt navn (your name)
- E-post (your e-mail)
- Emne (subject)
- Melding (message/description)

Our project should also include suggestion for handheld units (iPhone, iPad).
Updates

We have both been traveling with work for a while, and then unfortunately both of us got sick on return, so we need a few more days to evaluate and choose design. Kind Regards Arvid & Margit

Target Market(s)

Focus on therapy, learning, mastery and growth for children and teenagers with special needs, within the family dynamics, or in a group setting.
OUR MARKETS:
Private market: individuals, families, groups and health industry institutions (with focus on learning, mastery, growth (as well as growing up) and psychiatry for children and teenagers with special difficulties and needs)
Public institutions: Government institutions, state institutions and municipality institutions (e.g. schools, municipality health service, hospitals) that serve the public (families with children and teenagers with special needs, and where learning, mastery, growth (as well as growing up) and potential psychiatry is an issue).

Number of Pages Required

4 page

Font styles to use
Sans Serif

Colors

Designer to choose colors to be used in the design.

Requirements
Must have
• The website must have 4 pages with roll down curtain menus (we have added a PDF with suggested structure, and headings, with sub menus - see attached PDF drawing.
• The web page must also use the added logo file - and make the web page work well with our logo.
• We would like the website to have a modern look and we would like the site to be associated with typical HIGH END TOP QUALITY private health institutions, but with a stronger focus on human beings (hands, faces etc), and not white coats and doctors. We are psychologists in the private market.
• For instance, if photos are being used - we tend to like "warm" almost art-like, "grainy" two-tone (e.g. sepia) photos to illustrate our focus. If designer can find such photos as part of design, it would be interesting to us. We would like a few photos like that integrated in the design.
• We also want a design suggestion for how the web page should look like and behave on handheld units (e.g. iPhone, iPad).
Nice to have
• If designer could find a number of suitable photos that matches the business idea and design requirements (see description above), that could follow website, that would be good.
• It could also be nice to have graphic symbols that denote the different pages/subpages (subjects)....
• HORSES: we sometimes use horses as a "tool" in therapy sessions. The horse is not necessarily used for riding, but for contact, communication and grooming. PHOTOS: we would like the designer to find an opportunity for using a photo reflecting this cooperation between therapist, child, teenager and horse. It is a bit up to the designer to find a way to do this... Since the horse is only a tool, among many other tools, it does not have to be much - but we want to try and see how it will work with a photo that also reflects this part of our business.

```html
<!DOCTYPE html>
<html lang="no">
<head>
<meta charset="utf-8">
<title>Fjordlys og Samhold – Psykolog</title>
<link href="https://fonts.googleapis.com/css2?family=Oswald:wght@600&family=Poppins:wght@400;500&family=Libre+Baskerville:wght@400;700&display=swap" rel="stylesheet">
<style>
:root{
  --blue:#2f3b97;
  --blue-dark:#26307f;
  --green:#0b6a37;
  --green-pale:#e6efe9;
  --text:#4a4a4a;
  --muted:#666;
  --line:#e3e3e3;
  --white:#fff;
}
*{box-sizing:border-box;margin:0;padding:0}
html,body{width:1200px;height:3453px;overflow:hidden;background:var(--white)}
body{position:relative;font-family:'Poppins',sans-serif;color:var(--text)}
.shapes{position:absolute;left:0;top:0;width:1200px;height:3453px}
.abs{position:absolute}
.serif{font-family:'Libre Baskerville',serif;color:var(--blue)}
/* header */
.brand{left:76px;top:24px;display:flex;align-items:center;gap:10px;font-weight:500;font-size:17px;color:var(--blue)}
.brand-dot{width:14px;height:14px;border-radius:50%;background:var(--green)}
.nav{right:76px;top:36px;display:flex;gap:28px;font-size:16px;color:var(--white);align-items:center}
.search{width:16px;height:16px}
/* buttons */
.btn{display:flex;align-items:center;justify-content:center;background:var(--green);color:var(--white);
  font-family:'Libre Baskerville',serif;font-size:20px;border-radius:30px;box-shadow:6px 0 0 var(--blue)}
/* hero */
.hero-title{left:78px;top:282px;font-family:'Oswald',sans-serif;font-weight:600;font-size:56px;line-height:58px;color:var(--blue);letter-spacing:.5px}
.hero-text{left:79px;top:408px;font-size:16px;line-height:27px;color:#333;width:340px}
.hero-btn{left:78px;top:477px;width:212px;height:51px}
.hero-green{left:540px;top:190px;width:500px;height:440px;border-radius:50% 48% 45% 55%/52% 50% 50% 48%;background:var(--green)}
.hero-photo{left:556px;top:184px;width:500px;height:432px;border-radius:52% 48% 44% 56%/55% 48% 52% 45%;
  background:linear-gradient(120deg,#f4e6d2 0%,#d9a56a 40%,#7b4a2a 70%,#c8922a 100%)}
.deco-ring{border:2px solid;border-radius:50%}
.deco-sq{border:2px solid #b9c3e3;transform:rotate(20deg);width:14px;height:14px}
/* about */
.about-green{left:378px;top:782px;width:187px;height:130px;background:var(--green)}
.about-photo{left:125px;top:799px;width:422px;height:334px;border-radius:4px;
  background:linear-gradient(135deg,#dfe7ef,#aebccc 50%,#c9a0a4)}
.h2{font-size:40px}
.about-title{left:628px;top:842px}
.about-text{left:631px;top:906px;width:460px;font-size:15px;line-height:27px;color:var(--muted)}
.about-btn{left:630px;top:1059px;width:171px;height:51px}
/* services */
.svc-title{left:0;width:1200px;top:1335px;text-align:center}
.svc-sub{left:350px;width:500px;top:1394px;text-align:center;font-size:15px;line-height:27px;color:var(--muted)}
.svc{top:1482px;width:250px;text-align:center}
.svc-icon{width:120px;height:120px;margin:0 auto}
.svc h3{font-family:'Libre Baskerville',serif;color:var(--blue);font-size:21px;font-weight:700;margin-top:28px}
.svc p{font-size:15px;line-height:25.5px;color:var(--muted);margin-top:14px}
.svc a{display:inline-block;margin-top:12px;font-family:'Libre Baskerville',serif;font-size:14px;font-weight:700;color:var(--green);text-decoration:none}
/* news */
.news-title{left:80px;top:1990px}
.news-date{left:76px;top:2070px;display:flex;align-items:center;gap:12px;font-family:'Libre Baskerville',serif;font-size:15px;color:var(--green)}
.news-head{left:80px;top:2112px;width:420px;font-weight:500;font-size:19px;line-height:32px;color:#111}
.news-text{left:78px;top:2186px;width:410px;font-size:15px;line-height:27px;color:var(--muted)}
.news-btn{left:78px;top:2312px;width:171px;height:51px}
.news-green{left:569px;top:2253px;width:124px;height:130px;background:var(--green)}
.news-photo{left:590px;top:2033px;width:437px;height:332px;border-radius:4px;
  background:linear-gradient(120deg,#e9e4dc,#d8b38a 45%,#7e9fd8 75%,#f0ece6)}
/* contact */
.contact-title{left:0;width:1200px;top:2480px;text-align:center}
.contact-sub{left:0;width:1200px;top:2535px;text-align:center;font-size:18px;color:#555}
.field{left:361px;width:478px;height:51px;border:1px solid var(--line);border-left:4px solid var(--green);
  font-size:14px;color:#666;padding:14px 20px}
.field.msg{height:102px}
.send-btn{left:512px;top:2901px;width:171px;height:51px}
/* footer */
.foot-brand{left:74px;top:3258px;width:240px;text-align:center;font-size:30px;font-weight:500;color:var(--white);line-height:40px}
.foot-col{top:3132px}
.foot-col h4{font-family:'Libre Baskerville',serif;font-size:20px;font-weight:700;color:var(--blue);margin-bottom:26px}
.foot-col ul{list-style:none}
.foot-col li{font-size:15px;color:#555;height:31px;display:flex;align-items:center;gap:14px}
.foot-col li::before{content:"";width:5px;height:5px;border-radius:50%;background:var(--green);margin-left:6px}
.contact-list li::before{display:none}
.contact-list svg{width:20px;height:20px}
.socials{display:flex;gap:7px;margin-top:16px}
.social{width:42px;height:42px;border-radius:50%;background:var(--blue);display:flex;align-items:center;justify-content:center}
.social svg{width:20px;height:20px}
.foot-line{left:520px;top:3373px;width:604px;height:1px;background:var(--line)}
.copy{left:483px;width:734px;top:3403px;text-align:center;font-size:16px;color:#444}
</style>
</head>
<body>

<svg class="shapes" viewBox="0 0 1200 3453" aria-hidden="true">
  <path d="M375,0 L1200,0 L1200,677 C1100,660 980,600 880,520 C760,420 710,280 690,200 C670,120 560,30 375,0 Z" fill="#2f3b97"/>
  <path d="M905,105 C1030,140 1120,210 1200,310 L1200,340 C1120,240 1020,155 905,105 Z" fill="#fff"/>
  <path d="M0,717 C150,760 260,900 360,1000 C420,1060 480,1110 545,1198 C420,1290 200,1340 0,1320 Z" fill="#2f3b97"/>
  <path d="M0,1080 C120,1160 260,1200 400,1212 C260,1220 110,1190 0,1125 Z" fill="#fff"/>
  <path d="M655,1970 C780,1880 1000,1840 1200,1844 L1200,2454 C1100,2400 1020,2250 960,2100 C900,2000 800,1960 655,1970 Z" fill="#2f3b97"/>
  <path d="M805,1972 C950,1972 1080,2020 1200,2130 L1200,2160 C1080,2040 950,1985 805,1972 Z" fill="#fff"/>
  <circle cx="1100" cy="2860" r="150" fill="#f3f6f4"/>
  <path d="M0,2984 C170,3010 320,3110 385,3210 C430,3290 510,3400 585,3453 L0,3453 Z" fill="#2f3b97"/>
  <path d="M0,3360 C120,3390 250,3400 385,3398 C250,3410 110,3400 0,3385 Z" fill="#fff"/>
</svg>

<div class="abs brand"><span class="brand-dot"></span>Fjordlys og Samhold</div>
<nav class="abs nav">
  <span>Om Fjordlys og Samhold</span><span>Tjenester</span><span>Aktuelt</span><span>Kontakt</span>
  <svg class="search" viewBox="0 0 16 16"><circle cx="6.5" cy="6.5" r="5" fill="none" stroke="#fff" stroke-width="1.6"/><path d="M10.5 10.5 15 15" stroke="#fff" stroke-width="1.8"/></svg>
</nav>

<div class="abs deco-ring" style="left:314px;top:119px;width:13px;height:13px;border-color:#b9c3e3"></div>
<div class="abs deco-sq" style="left:512px;top:291px"></div>
<div class="abs deco-sq" style="left:423px;top:646px"></div>
<div class="abs deco-ring" style="left:-2px;top:482px;width:26px;height:26px;border-color:#7fb08f"></div>
<h1 class="abs hero-title">PSYKOLOG<br>MASTERY THERAPY</h1>
<p class="abs hero-text">Lorem Ipsum is simply dummy text of the printing and typesetting industry.</p>
<div class="abs btn hero-btn">Avtale et Møte</div>
<div class="abs hero-green"></div>
<div class="abs hero-photo" role="img" aria-label="Warm photo of a smiling girl and a woman facing each other"></div>

<div class="abs about-green"></div>
<div class="abs about-photo" role="img" aria-label="Photo of a therapist talking with a teenage boy in a bright office"></div>
<h2 class="abs serif h2 about-title">Om Fjordlys og Samhold</h2>
<p class="abs about-text">Lorem Ipsum is simply dummy text of the printing and typesetting industry. Lorem Ipsum has been the industry's standard dummy text ever since the 1500s, when an unknown printer took a galley of type and scrambled it to make a type specimen book it has survived not only.</p>
<div class="abs btn about-btn">Lære mer</div>

<h2 class="abs serif h2 svc-title">Vår Tjenester</h2>
<p class="abs svc-sub">Lorem Ipsum is simply dummy text of the printing and typesetting industry. Lorem Ipsum has been the industry</p>

<div class="abs svc" style="left:83px">
  <svg class="svc-icon" viewBox="0 0 120 120"><ellipse cx="58" cy="55" rx="58" ry="50" fill="#e6efe9"/><circle cx="66" cy="62" r="50" fill="#fff" stroke="#0b6a37" stroke-width="2.5"/><g fill="none" stroke="#0b6a37" stroke-width="2"><ellipse cx="66" cy="62" rx="26" ry="10"/><ellipse cx="66" cy="62" rx="26" ry="10" transform="rotate(60 66 62)"/><ellipse cx="66" cy="62" rx="26" ry="10" transform="rotate(-60 66 62)"/><circle cx="66" cy="62" r="5"/></g></svg>
  <h3>Utredning</h3>
  <p>Lorem Ipsum is simply dummy text of the printing and type setting industry.</p>
  <a>Learn More ▸</a>
</div>
<div class="abs svc" style="left:344px">
  <svg class="svc-icon" viewBox="0 0 120 120"><ellipse cx="58" cy="55" rx="58" ry="50" fill="#e6efe9"/><circle cx="66" cy="62" r="50" fill="#fff" stroke="#0b6a37" stroke-width="2.5"/><g fill="none" stroke="#0b6a37" stroke-width="2"><rect x="44" y="42" width="44" height="32" rx="2"/><path d="M38 80h56M52 50h28M52 57h28M52 64h18"/></g></svg>
  <h3>Rådgivning</h3>
  <p>Lorem Ipsum is simply dummy text of the printing and type setting industry.</p>
  <a>Learn More ▸</a>
</div>
<div class="abs svc" style="left:606px">
  <svg class="svc-icon" viewBox="0 0 120 120"><ellipse cx="58" cy="55" rx="58" ry="50" fill="#e6efe9"/><circle cx="66" cy="62" r="50" fill="#fff" stroke="#0b6a37" stroke-width="2.5"/><g fill="none" stroke="#0b6a37" stroke-width="2"><path d="M52 88V76c-8-5-12-12-10-22 2-11 12-18 24-17 13 1 21 11 20 23l5 8h-6v8h-10v12"/><circle cx="66" cy="56" r="8"/><circle cx="66" cy="56" r="3"/></g></svg>
  <h3>Kurs og work shops</h3>
  <p>Lorem Ipsum is simply dummy text of the printing and type setting industry.</p>
  <a>Learn More ▸</a>
</div>
<div class="abs svc" style="left:867px">
  <svg class="svc-icon" viewBox="0 0 120 120"><ellipse cx="58" cy="55" rx="58" ry="50" fill="#e6efe9"/><circle cx="66" cy="62" r="50" fill="#fff" stroke="#0b6a37" stroke-width="2.5"/><g fill="none" stroke="#0b6a37" stroke-width="2"><circle cx="66" cy="66" r="10"/><path d="M50 92c2-9 8-14 16-14s14 5 16 14M66 50V36M56 52l-8-10M76 52l8-10M62 38l4-4 4 4M46 46v-5h5M86 46v-5h-5"/></g></svg>
  <h3>Terapi og utvikling</h3>
  <p>Lorem Ipsum is simply dummy text of the printing and type setting industry.</p>
  <a>Learn More ▸</a>
</div>

<h2 class="abs serif h2 news-title">Siste Aktuelt</h2>
<div class="abs news-date">
  <svg width="18" height="18" viewBox="0 0 18 18"><rect x="1" y="3" width="16" height="14" rx="1" fill="none" stroke="#0b6a37" stroke-width="1.6"/><path d="M1 7h16M5 1v4M13 1v4M5 10h2M9 10h2M13 10h1M5 13h2M9 13h2" stroke="#0b6a37" stroke-width="1.6"/></svg>
  07 February 2020
</div>
<p class="abs news-head">Lorem Ipsum is simply dummy text of the printing and typesetting</p>
<p class="abs news-text">Lorem Ipsum is simply dummy text of the printing and typesetting industry. Lorem Ipsum has been the industry's standard dummy text ever since the 1500s, when an unknown printer took a galley .</p>
<div class="abs btn news-btn">Lære mer</div>
<div class="abs news-green"></div>
<div class="abs news-photo" role="img" aria-label="Photo of a woman and a young boy stretching an exercise band together"></div>
<svg class="abs" style="left:922px;top:2392px" width="84" height="16" viewBox="0 0 84 16"><path d="M2 8h32M8 2 2 8l6 6" fill="none" stroke="#888" stroke-width="1.5"/><path d="M50 8h32M76 2l6 6-6 6" fill="none" stroke="#2f3b97" stroke-width="1.5"/></svg>

<h2 class="abs serif h2 contact-title">Kontakt Oss</h2>
<p class="abs contact-sub">Hvis du har spørsmål til oss i dag!</p>
<div class="abs field" style="top:2599px">Ditt navn *</div>
<div class="abs field" style="top:2661px">E-post*</div>
<div class="abs field" style="top:2723px">Emne*</div>
<div class="abs field msg" style="top:2786px">Melding*</div>
<div class="abs btn send-btn">Sende inn</div>

<div class="abs foot-brand">Fjordlys og Samhold</div>
<div class="abs foot-col" style="left:471px">
  <h4>Sitemap</h4>
  <ul><li>Om Fjordlys og Samhold</li><li>Tjenester</li><li>Aktuelt</li><li>Kontakt</li></ul>
</div>
<div class="abs foot-col" style="left:699px">
  <h4>Vår Tjenester</h4>
  <ul><li>Utredning</li><li>Rådgivning</li><li>Kurs og work shops</li><li>Terapi og utvikling</li></ul>
</div>
<div class="abs foot-col" style="left:916px">
  <h4>Hold kontakten</h4>
  <ul class="contact-list">
    <li><svg viewBox="0 0 20 20"><path d="M4 2l4 1 1 4-2 2c1 2 3 4 5 5l2-2 4 1 1 4-2 2C9 18 2 11 2 4z" fill="#0b6a37"/></svg>987 65 432</li>
    <li><svg viewBox="0 0 20 20"><rect x="1" y="4" width="18" height="12" rx="1" fill="#0b6a37"/><path d="M1 5l9 6 9-6" fill="none" stroke="#fff" stroke-width="1.4"/></svg>post@fjordlys.no</li>
  </ul>
  <div class="socials" aria-label="Sosiale medier">
    <span class="social"><svg viewBox="0 0 20 20"><g fill="#fff"><circle cx="5" cy="10" r="2.6"/><circle cx="15" cy="4.5" r="2.6"/><circle cx="15" cy="15.5" r="2.6"/></g><path d="M5 10 15 4.5M5 10l10 5.5" stroke="#fff" stroke-width="1.6"/></svg></span>
    <span class="social"><svg viewBox="0 0 20 20"><path d="M3 4h14v9H8l-4 3v-3H3z" fill="#fff"/></svg></span>
    <span class="social"><svg viewBox="0 0 20 20"><g fill="none" stroke="#fff" stroke-width="1.6"><circle cx="10" cy="10" r="7.5"/><ellipse cx="10" cy="10" rx="3.2" ry="7.5"/><path d="M2.5 10h15"/></g></svg></span>
  </div>
</div>
<div class="abs foot-line"></div>
<p class="abs copy">©Fjordlys Og Samhold -2020 Alle rettigheter forbeholdt</p>

</body>
</html>
```